Australian Wine Online Sales website

We need to build an online presence for our export wine business 'Lanmeixo' that targets Australian wine to the Chinese consumer. Ideally the website will have look and feel of Western elegance and sophistication, but also build the personal brand of the Owner. The Chinese buying segment like to connect with their personal buyer in Australia. They need to see and feel authenticity and trust of the proprietor of the online sales business. We have direct access to the Australia wine producers, vineyards and the story of each wine producer and their products. This needs to be matched with a pictorial sales-cart so the owner can upload, describe and price the products, and the customer can read/browse and purchase items in the cart, possibly with provision for shipping costs, promotions, vouchers, referral/affiliate commission, and cross-links to social and business pages such as Talkora, Qinlu and Streamly & Snapvista, multiple payments terms and currencies (including Paxio and TalkoraPay). The site must have a feel of young, sophisticated elegance - not 'Old World' but 'New World' adventure and opportunity. Our physical presence is in Western Australia. A list of wineries in this region and their wines are found here: https://en.vinoreference.org/wiki/Register_of_cellars_in_Western_Australia
Updates

Hello Everyone, I appreciated all your participation and hard work. Maybe I didn't explain very well. It is very hard for me to comment on every of your design, because they are all similar and basic, not the design I like. We want to be an online shop has a smaller range of wines at the beginning, mainly are Australian wines. I have a hand drawing the design I preferred for the home page, to attract customers to know our wine collection better. I will try to upload them today. Great thanks to all of you. Margaret

Target Market(s)

Chinese young adult wine consumer

Industry/Entity Type

Winery

Coding

Coded - Design and coding required

Number of Pages Required

3 page

Font styles to use
Serif
Sans Serif
Decorative

Colors

Designer to choose colors to be used in the design.

Requirements
Must have
• Wine pictures and pictures of Margaret Zhou
• Shopping Cart
• sophisticated New World Australia feel
Nice to have
• Map links to winery locations
Should not have
• Poor taste

```html
<!DOCTYPE html>
<html lang="en">
<head>
<meta charset="utf-8">
<title>Lanmeixo – Australian Wine</title>
<link href="https://fonts.googleapis.com/css2?family=Source+Sans+3:wght@300;400;600;700&display=swap" rel="stylesheet">
<style>
:root{
  --blue:#0ba3e2;
  --blue-soft:#3ab8ea;
  --red:#e3171c;
  --gold:#f3a21d;
  --dark:#2b2b2b;
  --darker:#1d1d1d;
  --ink:#222;
  --grey:#777;
  --white:#fff;
}
*{box-sizing:border-box;margin:0;padding:0}
html,body{width:1200px;height:5017px;overflow:hidden}
body{font-family:"Source Sans 3",Arial,sans-serif;color:var(--ink);background:var(--white);position:relative}
.abs{position:absolute}
section,header,footer{position:absolute;left:0;width:1200px}

/* header + hero */
.hero{top:0;height:637px;background:linear-gradient(180deg,#1b2412 0%,#3d4a22 30%,#5b6a2c 55%,#2c3418 100%)}
.hero-photo{position:absolute;inset:0;background:radial-gradient(ellipse at 78% 70%,rgba(20,25,12,.75),transparent 45%),linear-gradient(180deg,rgba(0,0,0,.45),rgba(0,0,0,.15) 50%,rgba(0,0,0,.35))}
.brand{left:107px;top:15px;display:flex;align-items:center;gap:6px;color:var(--white);font-weight:700;font-size:13px;white-space:nowrap}
.brand-dot{width:34px;height:34px;border-radius:50%;border:2px solid var(--blue)}
.nav{left:0;top:23px;width:1200px;height:20px}
.nav a{position:absolute;color:var(--white);text-decoration:none;font-size:13px}
.nav-icon{top:22px;width:20px;height:20px}
.hero-title{top:254px;left:0;width:1200px;text-align:center;color:var(--white);font-weight:600;font-size:62px;line-height:60px;letter-spacing:3px}
.btn{display:flex;align-items:center;justify-content:center;font-weight:700;text-transform:uppercase;color:var(--white);text-decoration:none}
.btn-outline{border:2px solid var(--white);font-size:14px}
.btn-blue{background:var(--blue);font-size:14px}

/* categories */
.categories{top:610px;left:94px;width:1012px;height:91px;background:var(--white);box-shadow:0 4px 18px rgba(0,0,0,.12)}
.cat{position:absolute;top:0;height:91px;display:flex;align-items:center;gap:10px;font-weight:700;font-size:14px;color:var(--ink)}
.cat-icon{width:34px;height:34px;border-radius:50%;background:var(--blue-soft)}
.cat-sep{position:absolute;top:20px;width:1px;height:52px;background:#ddd}

/* about */
.about{top:637px;height:640px}
.about-bg{left:0;top:0;width:799px;height:520px;background:linear-gradient(90deg,#2a2a2a 0%,#333 55%,#1e1e1e 100%)}
.about-photo{left:651px;top:136px;width:455px;height:491px;background:linear-gradient(160deg,#3b3f44,#6e6a66 45%,#c9b8a4 70%,#2e3236)}
.play{left:95px;top:128px}
.section-h{font-weight:400;font-size:36px;letter-spacing:1px}
.about-h{left:95px;top:208px;color:var(--white)}
.about-text{left:95px;top:278px;width:510px;color:#ddd;font-size:10.5px;line-height:25px}
.about-btn{left:95px;top:411px;width:154px;height:43px;font-size:15px}

/* wines */
.wines-h{top:1294px;left:95px;color:var(--ink)}
.accent{color:var(--blue)}
.card{position:absolute;width:234px;height:516px;background:var(--white);box-shadow:0 1px 8px rgba(0,0,0,.14);text-align:center}
.bottle{position:absolute;left:34px;top:29px;width:166px;height:273px;background:linear-gradient(180deg,#eef7fb 0%,#cfeaf6 55%,#9fd6ee 100%)}
.wine-name{position:absolute;top:311px;width:100%;font-size:16px;color:#333}
.wine-region{position:absolute;top:339px;width:100%;font-size:12px;color:var(--grey)}
.stars{position:absolute;top:364px;width:100%;font-size:13px;color:var(--gold);letter-spacing:3px}
.price{position:absolute;top:400px;width:100%;font-size:20px;font-weight:700}
.card-btn{position:absolute;top:450px;height:29px;width:97px;font-size:9px;font-weight:700;color:var(--white);display:flex;align-items:center;justify-content:center}
.quick{left:16px;background:var(--blue)}
.cart{left:123px;background:var(--red)}

/* blog */
.blog{top:2515px;height:649px;background:var(--dark)}
.blog-h{left:95px;top:92px;color:var(--white)}
.view-all{left:500px;top:106px;display:flex;align-items:center;gap:10px;color:var(--white);font-size:13px}
.plus{width:28px;height:28px;border-radius:50%;background:var(--white);color:var(--ink);font-weight:700;display:flex;align-items:center;justify-content:center}
.blog-photo{left:95px;top:152px;width:513px;height:387px;background:linear-gradient(180deg,#8a8a83 0%,#c7c1b3 35%,#5b5547 60%,#1d2018 100%)}
.blog-date{left:653px;top:182px;color:#ccc;font-size:11px;text-decoration:underline}
.blog-title{left:653px;top:210px;color:var(--white);font-size:17px;font-weight:700}
.blog-text{left:653px;top:247px;width:453px;color:#ccc;font-size:10.5px;line-height:19.5px}
.blog-btn{left:653px;top:462px;width:185px;height:42px;font-size:15px}

/* members */
.members-h{top:3246px;left:0;width:1200px;text-align:center}
.member{position:absolute;top:3306px;height:475px;background:#f4f4f4;box-shadow:0 1px 8px rgba(0,0,0,.1);overflow:hidden}
.member-photo{position:absolute;inset:0;background:linear-gradient(180deg,#f7f7f7 0%,#ece6e0 45%,#d9ccc2 100%)}
.member-tag{position:absolute;left:0;bottom:0;width:320px;height:142px;background:var(--blue);clip-path:polygon(0 22%,100% 0,100% 100%,0 100%)}
.member-name{position:absolute;left:22px;top:60px;color:var(--white);font-size:20px;font-weight:700;letter-spacing:1px}
.member-role{position:absolute;left:22px;top:90px;color:var(--white);font-size:14px;font-weight:600}
.member-soc{position:absolute;left:278px;width:22px;height:22px;border-radius:50%;background:var(--white)}

/* affiliate */
.affiliate{top:3781px;height:575px;background:var(--dark)}
.aff-h{left:95px;top:138px;color:var(--white)}
.aff-text{left:95px;top:212px;width:440px;color:#ddd;font-size:10.5px;line-height:25px}
.aff-btn{left:95px;top:351px;width:186px;height:43px;font-size:15px}
.video{left:582px;top:99px;width:524px;height:361px;background:linear-gradient(180deg,#6f6a5c 0%,#4a3b2a 40%,#2f2116 70%,#1b140e 100%)}
.video-bar{position:absolute;left:30px;right:20px;bottom:18px;height:24px;display:flex;align-items:center;gap:14px;color:var(--white)}
.pause{width:26px;height:24px;display:flex;gap:5px;align-items:center;justify-content:center}
.pause i{display:block;width:5px;height:16px;background:var(--white)}
.track{position:relative;flex:1;height:6px;background:rgba(255,255,255,.45)}
.track b{position:absolute;left:0;top:0;height:6px;width:12px;background:var(--blue)}
.time{position:absolute;left:0;top:-24px;background:var(--white);color:var(--ink);font-size:10px;padding:1px 3px}
.hd{font-size:13px;font-weight:700;color:var(--blue)}

/* newsletter */
.newsletter{top:4356px;height:249px;background:var(--white)}
.news-blue{left:569px;top:0;width:631px;height:249px;background:var(--blue)}
.news-h{left:112px;top:80px;font-size:36px;font-weight:400;color:var(--ink)}
.news-text{left:112px;top:135px;width:370px;font-size:10.5px;line-height:18px;color:var(--grey)}
.news-input{left:635px;top:76px;width:452px;height:43px;background:var(--white);font-size:11px;letter-spacing:1px;color:#555;padding:14px 20px}
.news-btn{left:635px;top:130px;width:189px;height:43px;background:var(--darker);color:var(--white);font-size:15px;letter-spacing:1px;display:flex;align-items:center;justify-content:center}

/* footer */
.footer{top:4605px;height:412px;background:linear-gradient(180deg,#191919,#262421 50%,#141414)}
.foot-h{position:absolute;top:82px;color:var(--white);font-size:21px;font-weight:400}
.foot-text{position:absolute;color:#bbb;font-size:10.5px;line-height:25px}
.foot-link{position:absolute;color:#bbb;font-size:10.5px}
.soc{position:absolute;top:269px;width:24px;height:24px;border-radius:50%;background:var(--white);border:3px solid var(--blue)}
.copyright{position:absolute;top:338px;left:0;width:1200px;text-align:center;color:#ccc;font-size:10.5px}
</style>
</head>
<body>

<header class="hero">
  <div class="hero-photo" role="img" aria-label="Vineyard rows at sunset with two wine bottles in the foreground"></div>
  <div class="abs brand"><span class="brand-dot"></span>Lanmeixo</div>
  <nav class="abs nav">
    <a style="left:226px">Home</a>
    <a style="left:302px">About Us</a>
    <a style="left:397px">All Wines</a>
    <a style="left:491px">Shop Extract</a>
    <a style="left:607px">Members</a>
    <a style="left:703px">Blogs &amp; News</a>
    <a style="left:824px">Contact Us</a>
    <a style="left:929px">Affiliate</a>
  </nav>
  <svg class="abs nav-icon" style="left:1055px" viewBox="0 0 20 20"><circle cx="10" cy="10" r="9" fill="none" stroke="#fff" stroke-width="1.5"/><circle cx="10" cy="8" r="3" fill="none" stroke="#fff" stroke-width="1.5"/><path d="M4.5 16c1.5-3 9.5-3 11 0" fill="none" stroke="#fff" stroke-width="1.5"/></svg>
  <svg class="abs nav-icon" style="left:1085px" viewBox="0 0 20 20"><circle cx="10" cy="10" r="9" fill="none" stroke="#fff" stroke-width="1.5"/><path d="M5 6h2l1.5 6h6l1-4.5H8" fill="none" stroke="#fff" stroke-width="1.3"/><circle cx="9" cy="14.5" r="1" fill="#fff"/><circle cx="14" cy="14.5" r="1" fill="#fff"/></svg>
  <h1 class="abs hero-title">ENJOY LIFE ENJOY THE<br>GOOD WINE WITH US</h1>
  <a class="abs btn btn-outline" style="left:427px;top:388px;width:152px;height:43px">Know More</a>
  <a class="abs btn btn-blue" style="left:588px;top:388px;width:185px;height:43px">Discover Wines</a>
</header>

<section class="about">
  <div class="abs about-bg" role="img" aria-label="Dim photo of a hand pouring wine"></div>
  <div class="abs about-photo" role="img" aria-label="Margaret Zhou standing beside a wine cellar rack"></div>
  <svg class="abs play" width="44" height="44" viewBox="0 0 44 44"><circle cx="22" cy="22" r="20" fill="none" stroke="#fff" stroke-width="2"/><path d="M18 14l11 8-11 8z" fill="#fff"/></svg>
  <h2 class="abs section-h about-h">ABOUT US</h2>
  <p class="abs about-text">Lanmeixo wine company was founded by several wine lovers including Margaret Zhou, Oliver Brandt, Ruoxi Han, Lena Wu, Sophie Tan in March 2016. The company is based in Perth, Western Australia. It was established specifically for the export of Australian wine to China, then globally. In past three years we travelled and visited several Australia famous wine regions including Margaret River and the Swan Valley in Western Australia.</p>
  <a class="abs btn btn-blue about-btn">Know More</a>
</section>

<div class="abs categories">
  <div class="cat" style="left:46px"><span class="cat-icon"></span>RED WINE</div>
  <span class="cat-sep" style="left:198px"></span>
  <div class="cat" style="left:225px"><span class="cat-icon"></span>WHITE WINE</div>
  <span class="cat-sep" style="left:393px"></span>
  <div class="cat" style="left:415px"><span class="cat-icon"></span>ROSE STYLE WINE</div>
  <span class="cat-sep" style="left:627px"></span>
  <div class="cat" style="left:650px"><span class="cat-icon"></span>SPARKLING &amp; CHAMPAGNE WINE</div>
</div>

<h2 class="abs section-h wines-h">LMX ALL <span class="accent">WINES</span></h2>

<div class="card" style="left:95px;top:1364px"><div class="bottle" role="img" aria-label="Product photo: bottle of Hollow Creek wine"></div><div class="wine-name">Hollow Creek</div><div class="wine-region">Yallingup</div><div class="stars">★★★★★</div><div class="price">$2,90 USD</div><div class="card-btn quick">Quick Shop</div><div class="card-btn cart">Add To Cart</div></div>
<div class="card" style="left:355px;top:1364px"><div class="bottle" role="img" aria-label="Product photo: bottle of Hollow Creek wine"></div><div class="wine-name">Hollow Creek</div><div class="wine-region">Yallingup</div><div class="stars">★★★★★</div><div class="price">$2,90 USD</div><div class="card-btn quick">Quick Shop</div><div class="card-btn cart">Add To Cart</div></div>
<div class="card" style="left:615px;top:1364px"><div class="bottle" role="img" aria-label="Product photo: bottle of Hollow Creek wine"></div><div class="wine-name">Hollow Creek</div><div class="wine-region">Yallingup</div><div class="stars">★★★★★</div><div class="price">$2,90 USD</div><div class="card-btn quick">Quick Shop</div><div class="card-btn cart">Add To Cart</div></div>
<div class="card" style="left:875px;top:1364px"><div class="bottle" role="img" aria-label="Product photo: bottle of Hollow Creek wine"></div><div class="wine-name">Hollow Creek</div><div class="wine-region">Yallingup</div><div class="stars">★★★★★</div><div class="price">$2,90 USD</div><div class="card-btn quick">Quick Shop</div><div class="card-btn cart">Add To Cart</div></div>
<div class="card" style="left:95px;top:1909px"><div class="bottle" role="img" aria-label="Product photo: bottle of Hollow Creek wine"></div><div class="wine-name">Hollow Creek</div><div class="wine-region">Yallingup</div><div class="stars">★★★★★</div><div class="price">$2,90 USD</div><div class="card-btn quick">Quick Shop</div><div class="card-btn cart">Add To Cart</div></div>
<div class="card" style="left:355px;top:1909px"><div class="bottle" role="img" aria-label="Product photo: bottle of Hollow Creek wine"></div><div class="wine-name">Hollow Creek</div><div class="wine-region">Yallingup</div><div class="stars">★★★★★</div><div class="price">$2,90 USD</div><div class="card-btn quick">Quick Shop</div><div class="card-btn cart">Add To Cart</div></div>
<div class="card" style="left:615px;top:1909px"><div class="bottle" role="img" aria-label="Product photo: bottle of Hollow Creek wine"></div><div class="wine-name">Hollow Creek</div><div class="wine-region">Yallingup</div><div class="stars">★★★★★</div><div class="price">$2,90 USD</div><div class="card-btn quick">Quick Shop</div><div class="card-btn cart">Add To Cart</div></div>
<div class="card" style="left:875px;top:1909px"><div class="bottle" role="img" aria-label="Product photo: bottle of Hollow Creek wine"></div><div class="wine-name">Hollow Creek</div><div class="wine-region">Yallingup</div><div class="stars">★★★★★</div><div class="price">$2,90 USD</div><div class="card-btn quick">Quick Shop</div><div class="card-btn cart">Add To Cart</div></div>

<section class="blog">
  <h2 class="abs section-h blog-h">BLOG <span class="accent">&amp; NEWS</span></h2>
  <div class="abs view-all">VIEW ALL <span class="plus">+</span></div>
  <div class="abs blog-photo" role="img" aria-label="Row of wine bottles on a shop shelf"></div>
  <div class="abs blog-date">May 28, 2019</div>
  <h3 class="abs blog-title">LMX NEWS</h3>
  <div class="abs blog-text">
    <p>Etiam eleifend fermentum libero, id dignissim metus pharetra sed. Vivamus vehicula convallis lorem, in iaculis risus molestie nec. In pellentesque, nisi sit amet hendrerit rutrum, sem quam dictum nibh, at viverra lectus neque non leo. Minim affert iudicabit ne mea, vel accumsan evertitur ut, ius te causae aliquip. Facer homero dolores ut eum, eos no sale munere quaeque. Cu tota habeo percipit.</p>
    <p style="margin-top:6px">Etiam eleifend fermentum libero, id dignissim metus pharetra sed. Vivamus vehicula convallis lorem, in iaculis risus molestie nec. In pellentesque, nisi sit amet hendrerit rutrum, sem quam dictum nibh, at viverra lectus neque non leo. Minim affert iudicabit ne mea, vel accumsan evertitur ut, ius te causae aliquip. Facer homero dolores ut eum, eos no sale munere quaeque. Cu tota habeo percipit.</p>
  </div>
  <a class="abs btn btn-blue blog-btn">Know More</a>
</section>

<h2 class="abs section-h members-h">LMX ALL <span class="accent">MEMBERS</span></h2>
<div class="member" style="left:95px;width:320px">
  <div class="member-photo" role="img" aria-label="Portrait of a smiling company manager with arms crossed"></div>
  <div class="member-tag">
    <div class="member-name">JHON DOE</div>
    <div class="member-role">(COMPANY MANAGER)</div>
    <span class="member-soc" style="top:26px"></span>
    <span class="member-soc" style="top:60px"></span>
    <span class="member-soc" style="top:94px"></span>
  </div>
</div>
<div class="member" style="left:440px;width:320px"><div class="member-photo" role="img" aria-label="Portrait of a team member in a pink blouse"></div></div>
<div class="member" style="left:789px;width:317px"><div class="member-photo" role="img" aria-label="Portrait of a team member in a light shirt with arms crossed"></div></div>

<section class="affiliate">
  <h2 class="abs section-h aff-h">AFFILIATE</h2>
  <div class="abs aff-text">
    <p>Calling all Lanmeixo Loves whom wish to express to the world their love for our wines- we have the Lanmeixo platform for you!</p>
    <p>By joining our affiliate program you can upload our banners or product links to any of your social media platforms which may include your Talkora, Qinlu, Clipstream channel, blog or website and receive a commission for every sale.</p>
  </div>
  <a class="abs btn btn-blue aff-btn">Know More</a>
  <div class="abs video" role="img" aria-label="Video of a vaulted wine cellar with barrels and a tasting counter">
    <div class="video-bar">
      <div class="pause"><i></i><i></i></div>
      <div class="track"><b></b><span class="time">00:08</span></div>
      <span class="hd">HD</span>
    </div>
  </div>
</section>

<section class="newsletter">
  <div class="abs news-blue"></div>
  <h2 class="abs news-h">Newsletter</h2>
  <p class="abs news-text">Subscribe to the Vinora mailing list to receive updates on new arrivals, special offers and other discount information.</p>
  <div class="abs news-input">Enter your mail id:</div>
  <div class="abs news-btn">SUBSCRIBE</div>
</section>

<footer class="footer" role="contentinfo">
  <h4 class="foot-h" style="left:95px">About Us</h4>
  <p class="foot-text" style="left:95px;top:122px;width:300px">Lanmeixo wine company was founded by several wine lovers including Margaret Zhou, Oliver Brandt, Ruoxi Han, Lena Wu, Sophie Tan in March 2016. The company is based in Perth, Western Australia.</p>
  <span class="soc" style="left:95px"></span><span class="soc" style="left:125px"></span><span class="soc" style="left:155px"></span><span class="soc" style="left:185px"></span>

  <h4 class="foot-h" style="left:479px">Navigate</h4>
  <span class="foot-link" style="left:483px;top:126px">Home</span>
  <span class="foot-link" style="left:483px;top:159px">About Us</span>
  <span class="foot-link" style="left:483px;top:192px">All Wines</span>
  <span class="foot-link" style="left:483px;top:225px">Shop Extract</span>
  <span class="foot-link" style="left:593px;top:126px">Members</span>
  <span class="foot-link" style="left:593px;top:159px">Blogs &amp; News</span>
  <span class="foot-link" style="left:593px;top:192px">Contact Us</span>
  <span class="foot-link" style="left:593px;top:225px">Affiliate</span>

  <h4 class="foot-h" style="left:752px">Support</h4>
  <span class="foot-link" style="left:756px;top:126px">Theme Features</span>
  <span class="foot-link" style="left:756px;top:159px">Shipping</span>
  <span class="foot-link" style="left:756px;top:192px">Returns</span>
  <span class="foot-link" style="left:756px;top:225px">About</span>

  <h4 class="foot-h" style="left:960px">Contact Info</h4>
  <svg class="abs" style="left:963px;top:126px" width="12" height="16" viewBox="0 0 12 16"><path d="M6 0a6 6 0 0 0-6 6c0 4.5 6 10 6 10s6-5.5 6-10a6 6 0 0 0-6-6z" fill="#fff"/><circle cx="6" cy="6" r="2.2" fill="#222"/></svg>
  <p class="foot-text" style="left:995px;top:118px;width:130px;line-height:20px">Lorem Ipsum, 8th Floor Dolor Lorem, Chaina D4K 1T7</p>
  <svg class="abs" style="left:963px;top:200px" width="12" height="16" viewBox="0 0 12 16"><path d="M3 0h3l1 4-2 1.5c.8 2 2 3.4 3.5 4.5L10 8l2 3-1 4C5 15 0 8 2 1z" fill="#fff"/></svg>
  <span class="foot-link" style="left:995px;top:201px">(+00) 123-456-7890</span>
  <svg class="abs" style="left:962px;top:241px" width="14" height="12" viewBox="0 0 14 12"><path d="M0 5L14 0 10 12 7 7z" fill="#fff"/></svg>
  <span class="foot-link" style="left:995px;top:239px">info@lanmeixo.com</span>

  <p class="copyright">© 2019 Lanmeixo. All rights reserved.</p>
</footer>

</body>
</html>
```